Tidal Spoon is a modern and professional services business in the field of hospitality.

Need business card for a professional chef and consultant. Attention to detail and to stand out is our goal. I want a professional and stand out card which is not generic.
Would like a modern card with black gold or blue I’m not very sure on colours yet , open to ideas from those in the know. This is my second project and have been really happy with the process so far.
With 15 years in the hospitality industry I am launching into consulting and starting my own business. I’d like a few types of designs to look at which style I want. Open to suggestions. Thanks in advance for the work. I want something that will become part of my brand as it is launched. There is a chance for possible future work to the right person.

Target Market(s)

Restauranters and Registered training organisations.

Industry/Entity Type

Professional Service

Font styles to use
Serif

Colors

Designer to choose colors to be used in the design.

Requirements
Must have
• A stand out design, blue / black
Nice to have
• Can u get embossed cards?
Should not have
• Na

```html
<!DOCTYPE html>
<html lang="en">
<head>
<meta charset="utf-8">
<title>Tidal Spoon – Business Card</title>
<link rel="stylesheet" href="https://fonts.googleapis.com/css2?family=Playfair+Display:ital,wght@1,600;1,700&family=Lora:wght@400&display=swap">
<style>
  :root {
    --page: #e6e6e6;
    --card-black: #000000;
    --weave-mid: #1f1f1f;
    --band-gold: #ecc04f;
    --text-gold: #e8b84a;
    --ink: #0a0a0a;
  }
  html, body {
    margin: 0;
    width: 1200px;
    height: 1200px;
    overflow: hidden;
    background: var(--page);
  }
  .card {
    position: absolute;
    left: 180px;
    top: 362px;
    width: 840px;
    height: 476px;
    background: var(--card-black);
    overflow: hidden;
  }
  .weave-texture {
    position: absolute;
    inset: 30px 60px 40px 60px;
    background: radial-gradient(ellipse at 55% 50%, var(--weave-mid) 0%, #111 45%, var(--card-black) 75%);
  }
  .name-band {
    position: absolute;
    left: 0;
    top: 131px;
    width: 378px;
    height: 243px;
    background: var(--band-gold);
    border-radius: 0 122px 122px 0;
  }
  .name-block {
    position: absolute;
    right: 78px;
    top: 80px;
    text-align: right;
    font-family: "Playfair Display", serif;
    font-style: italic;
    color: var(--ink);
  }
  .person-name {
    margin: 0;
    font-size: 42px;
    font-weight: 700;
    line-height: 1;
    white-space: nowrap;
  }
  .person-title {
    margin: 10px 0 0;
    font-size: 19px;
    font-weight: 600;
    white-space: nowrap;
  }
  .contact-list {
    position: absolute;
    left: 0;
    top: 0;
    margin: 0;
    padding: 0;
    list-style: none;
    font-family: "Lora", serif;
    color: var(--text-gold);
    font-size: 18px;
    line-height: 1;
  }
  .contact-item { position: absolute; left: 0; }
  .contact-icon {
    position: absolute;
    left: 414px;
    width: 32px;
    height: 32px;
    fill: var(--text-gold);
  }
  .contact-lines {
    position: absolute;
    left: 470px;
    white-space: nowrap;
  }
  .contact-lines span { display: block; }
  .item-phone .contact-icon { top: 154px; }
  .item-phone .contact-lines { top: 146px; }
  .item-phone .contact-lines span + span { margin-top: 11px; }
  .item-web .contact-icon { top: 232px; }
  .item-web .contact-lines { top: 224px; }
  .item-web .contact-lines span + span { margin-top: 14px; }
  .item-address .contact-icon { top: 316px; }
  .item-address .contact-lines { top: 310px; }
  .item-address .contact-lines span + span { margin-top: 11px; }
</style>
</head>
<body>
  <main class="card">
    <div class="weave-texture" role="img" aria-label="Dark woven wood texture background"></div>

    <div class="name-band">
      <div class="name-block">
        <h1 class="person-name">Boss Chef</h1>
        <p class="person-title">Chef &amp; Consultant</p>
      </div>
    </div>

    <ul class="contact-list">
      <li class="contact-item item-phone">
        <svg class="contact-icon" viewBox="0 0 24 24" aria-hidden="true">
          <path d="M6.6 10.8c1.4 2.8 3.8 5.1 6.6 6.6l2.2-2.2c.3-.3.7-.4 1-.2 1.1.4 2.3.6 3.6.6.6 0 1 .4 1 1V20c0 .6-.4 1-1 1C10.6 21 3 13.4 3 4c0-.6.4-1 1-1h3.5c.6 0 1 .4 1 1 0 1.3.2 2.5.6 3.6.1.3 0 .7-.2 1z"/>
        </svg>
        <div class="contact-lines">
          <span>+1 555 0142 7789</span>
          <span>+1 555 0187 7684</span>
        </div>
      </li>
      <li class="contact-item item-web">
        <svg class="contact-icon" viewBox="0 0 24 24" aria-hidden="true">
          <path d="M12 2a10 10 0 1 0 0 20 10 10 0 0 0 0-20zm0 2.2a7.8 7.8 0 0 1 5.6 2.4h-2.3l-1.2 1.5-1.8-.3-.9 1.4 1.4 1.2-1 1.7-2.4-.6-1.6 1.5.7 2.6 2 .9-.4 2.4A7.8 7.8 0 0 1 4.3 10.6l2.3.8 1.4-1.6-.5-2.2 1.8-1.4L9 4.8a7.8 7.8 0 0 1 3-.6zm6.8 4.4a7.8 7.8 0 0 1-2.6 10l.4-2.7 1.6-1.6-.8-2.3 1.4-1.4z"/>
        </svg>
        <div class="contact-lines">
          <span>INFO@TIDALSPOON.COM</span>
          <span>WWW.TIDALSPOON.COM</span>
        </div>
      </li>
      <li class="contact-item item-address">
        <svg class="contact-icon" viewBox="0 0 24 24" aria-hidden="true">
          <path d="M12 2a7 7 0 0 0-7 7c0 5 7 13 7 13s7-8 7-13a7 7 0 0 0-7-7zm0 2.2A4.8 4.8 0 0 1 16.8 9c0 2.9-3.1 7.4-4.8 9.6C10.3 16.4 7.2 11.9 7.2 9A4.8 4.8 0 0 1 12 4.2zm0 2.3a2.5 2.5 0 1 0 0 5 2.5 2.5 0 0 0 0-5z"/>
        </svg>
        <div class="contact-lines">
          <span>YOUR CITY ADDRESS</span>
          <span>HARBOUR ST, PORT CITY, USA</span>
        </div>
      </li>
    </ul>
  </main>
</body>
</html>
```